Doorhanger logo and design

Company is called "Beamwell TV" would like a logo created for it, with colors if red, white and blue. Example would be a tv with a remote or antenna ect...doorhanger size is 3.5x8.5 in which I am using quorvaprint.example so it needs to fit within the size thanks.

Industry/Entity Type

Tv

```html
<!DOCTYPE html>
<html lang="en">
<head>
<meta charset="utf-8">
<title>Beamwell TV Door Hanger</title>
<link rel="stylesheet" href="https://fonts.googleapis.com/css2?family=Montserrat:wght@500;600;800&display=swap">
<style>
  :root {
    --page: #ece7df;
    --navy-deep: #12245a;
    --navy: #1c3576;
    --navy-light: #27488f;
    --sky: #2e8fd0;
    --sky-pale: #bfe3f5;
    --red: #e5202a;
    --white: #ffffff;
  }
  html, body {
    margin: 0;
    width: 1200px;
    height: 975px;
    overflow: hidden;
    background: var(--page);
    font-family: "Montserrat", Arial, sans-serif;
  }
  .stage {
    position: relative;
    width: 1200px;
    height: 975px;
  }
  .hanger {
    position: absolute;
    top: 73px;
    width: 329px;
    height: 806px;
    filter: drop-shadow(2px 3px 4px rgba(0,0,0,0.25));
  }
  .hanger--front { left: 244px; }
  .hanger--back  { left: 638px; }
  .brand-name {
    font-family: "Montserrat", Arial, sans-serif;
    font-weight: 800;
  }
  .brand-name--front { fill: var(--navy); font-size: 32px; }
  .brand-name--back  { fill: var(--white); font-size: 18px; }
  .brand-mark { fill: var(--red); }
  .contact-phone { fill: var(--white); font-weight: 600; font-size: 28px; }
  .contact-line  { fill: var(--white); font-weight: 500; font-size: 16px; }
  .contact-icon  { fill: var(--red); }
  .contact-glyph { fill: none; stroke: var(--white); stroke-width: 1.6; stroke-linecap: round; stroke-linejoin: round; }
</style>
</head>
<body>
<main class="stage">

  <!-- Front panel -->
  <svg class="hanger hanger--front" viewBox="0 0 383 940" aria-label="Beamwell TV door hanger, front">
    <defs>
      <linearGradient id="front-body" x1="0" y1="0" x2="0" y2="1">
        <stop offset="0" stop-color="var(--navy)"/>
        <stop offset="1" stop-color="var(--navy-deep)"/>
      </linearGradient>
      <linearGradient id="front-cap" x1="0" y1="0" x2="0" y2="1">
        <stop offset="0" stop-color="var(--navy)"/>
        <stop offset="1" stop-color="var(--navy-light)"/>
      </linearGradient>
      <linearGradient id="front-accent" x1="1" y1="0" x2="0" y2="1">
        <stop offset="0" stop-color="var(--sky)"/>
        <stop offset="0.6" stop-color="var(--navy-light)"/>
        <stop offset="1" stop-color="var(--sky)"/>
      </linearGradient>
      <linearGradient id="front-pixels" x1="0" y1="0" x2="0" y2="1">
        <stop offset="0" stop-color="var(--navy-deep)" stop-opacity="0"/>
        <stop offset="0.35" stop-color="#2a5fa8" stop-opacity="0.35"/>
        <stop offset="0.6" stop-color="#3a7cc4" stop-opacity="0.75"/>
        <stop offset="0.8" stop-color="#b3283f" stop-opacity="0.8"/>
        <stop offset="1" stop-color="#1d4f9a" stop-opacity="0.9"/>
      </linearGradient>
      <radialGradient id="front-glow" cx="0.5" cy="0.55" r="0.5">
        <stop offset="0" stop-color="#3f8fd4" stop-opacity="0.45"/>
        <stop offset="1" stop-color="#3f8fd4" stop-opacity="0"/>
      </radialGradient>
      <mask id="front-cut">
        <rect width="383" height="940" fill="#fff"/>
        <circle cx="191" cy="141" r="109" fill="#000"/>
        <polygon points="113,0 139,0 146,48 124,52" fill="#000"/>
      </mask>
    </defs>
    <g mask="url(#front-cut)">
      <rect class="panel-body" width="383" height="940" fill="url(#front-body)"/>
      <path class="panel-cap" d="M0,0 H383 V112 Q191,190 0,122 Z" fill="url(#front-cap)"/>
      <path class="swoosh-accent" d="M383,240 C240,246 60,340 0,455 V726 C190,726 330,650 383,520 Z" fill="url(#front-accent)"/>
      <path class="swoosh-highlight" d="M383,262 C250,270 70,360 0,466 V700 C170,702 318,640 383,508 Z" fill="var(--sky-pale)"/>
      <path class="swoosh-white" d="M383,272 C250,280 75,368 0,470 V690 C165,692 312,632 383,500 Z" fill="var(--white)"/>
      <rect class="brand-mark" x="52" y="436" width="26" height="26"/>
      <text class="brand-name brand-name--front" x="88" y="461">Beamwell TV</text>
      <g class="pixel-field" role="img" aria-label="Scattered red and blue glowing pixel squares across the base">
        <rect y="730" width="383" height="210" fill="url(#front-pixels)"/>
        <ellipse cx="191" cy="860" rx="170" ry="90" fill="url(#front-glow)"/>
      </g>
    </g>
  </svg>

  <!-- Back panel -->
  <svg class="hanger hanger--back" viewBox="0 0 383 940" aria-label="Beamwell TV door hanger, back">
    <defs>
      <linearGradient id="back-body" x1="0" y1="0" x2="0" y2="1">
        <stop offset="0" stop-color="var(--navy)"/>
        <stop offset="1" stop-color="var(--navy-deep)"/>
      </linearGradient>
      <linearGradient id="back-cap" x1="0" y1="0" x2="0" y2="1">
        <stop offset="0" stop-color="var(--navy)"/>
        <stop offset="1" stop-color="var(--navy-light)"/>
      </linearGradient>
      <linearGradient id="back-pixels" x1="0" y1="0" x2="0" y2="1">
        <stop offset="0" stop-color="var(--navy-deep)" stop-opacity="0"/>
        <stop offset="0.35" stop-color="#2a5fa8" stop-opacity="0.35"/>
        <stop offset="0.6" stop-color="#3a7cc4" stop-opacity="0.75"/>
        <stop offset="0.8" stop-color="#b3283f" stop-opacity="0.8"/>
        <stop offset="1" stop-color="#1d4f9a" stop-opacity="0.9"/>
      </linearGradient>
      <radialGradient id="back-glow" cx="0.5" cy="0.55" r="0.5">
        <stop offset="0" stop-color="#3f8fd4" stop-opacity="0.45"/>
        <stop offset="1" stop-color="#3f8fd4" stop-opacity="0"/>
      </radialGradient>
      <mask id="back-cut">
        <rect width="383" height="940" fill="#fff"/>
        <circle cx="191" cy="141" r="109" fill="#000"/>
        <polygon points="244,0 270,0 258,52 236,48" fill="#000"/>
      </mask>
    </defs>
    <g mask="url(#back-cut)">
      <rect class="panel-body" width="383" height="940" fill="url(#back-body)"/>
      <path class="panel-cap" d="M0,0 H383 V112 Q191,190 0,122 Z" fill="url(#back-cap)"/>

      <rect class="brand-mark" x="120" y="327" width="14" height="14"/>
      <text class="brand-name brand-name--back" x="141" y="341">Beamwell TV</text>

      <g class="contact contact--phone">
        <circle class="contact-icon" cx="81" cy="502" r="14"/>
        <path class="contact-glyph" d="M75,495 q-1,5 4,11 q5,5 9,4 l1,-3 l-4,-3 l-2,2 q-3,-1 -5,-5 l2,-2 l-2,-4 Z"/>
        <text class="contact-phone" x="105" y="513">555-0142-7788</text>
      </g>
      <g class="contact contact--email">
        <circle class="contact-icon" cx="81" cy="549" r="14"/>
        <rect class="contact-glyph" x="74" y="544" width="14" height="10" rx="1"/>
        <path class="contact-glyph" d="M74,545 L81,550 L88,545"/>
        <text class="contact-line" x="110" y="555">hello@beamwelltv.example</text>
      </g>
      <g class="contact contact--web">
        <circle class="contact-icon" cx="81" cy="599" r="14"/>
        <circle class="contact-glyph" cx="81" cy="599" r="7.5"/>
        <path class="contact-glyph" d="M73.5,599 H88.5 M81,591.5 Q76,599 81,606.5 M81,591.5 Q86,599 81,606.5"/>
        <text class="contact-line" x="110" y="605">www.beamwelltv.example</text>
      </g>

      <g class="pixel-field" role="img" aria-label="Scattered red and blue glowing pixel squares across the base">
        <rect y="730" width="383" height="210" fill="url(#back-pixels)"/>
        <ellipse cx="191" cy="860" rx="170" ry="90" fill="url(#back-glow)"/>
      </g>
    </g>
  </svg>

</main>
</body>
</html>
```